Fresh, modern, fun business card for pediatric dental practice

Need a business card for fresh, modern, fun pediatric dental practice

Clean look that matches our website's font and colors

We prefer the look of curved corners on business cards

Target Market(s)

parents (mothers) of young children, professionals, mid-high class

Industry/Entity Type

Dental

Contact Information for Business Card

Maplewood Pediatric Dentistry
482 Corbett Lane
Suite 619
Hollis Springs, PA 17390
717.555.0193
www.maplewoodtotsdental.example

Mei-Hua Tran, DMD
Colette Margrave, DMD
(we are working on our email address, but we would like that on the card as well)

Font styles to use
Sans Serif

Requirements
Must have
• All info; we would also like to make cards for individual staff members
• colors from our website and color palatte, attatched
• use same font and design as website for branding
Nice to have
• clean, simple card that has a pop of color
• we would like to see a few designs with our tag line "where little smiles glow"
• we are not sure if we want to have it on there or not
• we would like to see a few designs incorporating the ribbon graphic on our website where the word WELCOME is

```html
<!DOCTYPE html>
<html lang="en">
<head>
<meta charset="utf-8">
<title>Maplewood Pediatric Dentistry – Business Card</title>
<link href="https://fonts.googleapis.com/css2?family=Lato:wght@400;700;900&display=swap" rel="stylesheet">
<style>
  :root {
    --magenta: #d6309b;
    --magenta-deep: #b81f82;
    --gold: #e9a923;
    --ink: #3a3a3a;
    --plum: #4b2546;
    --paper: #ffffff;
    --stage: #ecebe8;
  }
  * { box-sizing: border-box; margin: 0; padding: 0; }
  html, body { width: 1200px; height: 900px; overflow: hidden; }
  body {
    background: var(--stage);
    font-family: "Lato", sans-serif;
    position: relative;
  }
  .card {
    position: absolute;
    left: 250px;
    width: 700px;
    height: 400px;
    border-radius: 22px;
    overflow: hidden;
    box-shadow: 0 6px 18px rgba(0,0,0,0.18);
  }
  /* Back of card */
  .card-back { top: 40px; }
  .back-pattern {
    position: absolute; inset: 0;
    background: radial-gradient(circle at 55% 45%, #e23ca7 0%, var(--magenta) 45%, #c92a90 100%);
  }
  .back-name {
    position: absolute; left: 0; right: 0; top: 186px;
    text-align: center;
    color: #f7c9e6;
    font-weight: 700;
    font-size: 20px;
    letter-spacing: 0.5px;
  }
  /* Front of card */
  .card-front { top: 460px; background: var(--paper); }
  .brand {
    position: absolute; left: 40px; top: 160px; width: 290px;
    display: flex; align-items: center; gap: 12px;
  }
  .brand-dot {
    flex: none; width: 30px; height: 30px; border-radius: 50%;
    background: var(--gold);
  }
  .brand-name {
    color: var(--gold);
    font-weight: 900;
    font-size: 27px;
    line-height: 1.05;
  }
  .divider {
    position: absolute; left: 345px; top: 78px;
    width: 2px; height: 178px; background: var(--gold);
  }
  .details { position: absolute; left: 372px; top: 62px; right: 20px; }
  .doctor {
    color: var(--magenta);
    font-weight: 900;
    font-size: 22px;
    line-height: 1.2;
    white-space: nowrap;
  }
  .doctor .degree { color: var(--gold); font-weight: 400; }
  .address {
    margin-top: 14px;
    color: var(--ink);
    font-size: 14px;
    line-height: 1.35;
  }
  .contacts { list-style: none; margin-top: 14px; }
  .contacts li {
    display: flex; align-items: center; gap: 8px;
    color: var(--ink); font-size: 14px; line-height: 1; margin-bottom: 6px;
  }
  .contacts svg { flex: none; width: 18px; height: 18px; }
  .ribbon { position: absolute; left: 0; top: 282px; width: 700px; height: 70px; }
  .tagline {
    position: absolute; left: 300px; right: 40px; top: 303px;
    text-align: center;
    color: #fff; font-size: 18px; letter-spacing: 0.3px;
  }
</style>
</head>
<body>

<section class="card card-back" aria-label="Card back">
  <div class="back-pattern" role="img" aria-label="Magenta background with a faint repeating decorative pattern"></div>
  <p class="back-name">Maplewood Pediatric Dentistry</p>
</section>

<section class="card card-front" aria-label="Card front">
  <div class="brand">
    <span class="brand-dot"></span>
    <p class="brand-name">Maplewood Pediatric Dentistry</p>
  </div>

  <div class="divider"></div>

  <div class="details">
    <p class="doctor">Mei-Hua Tran, <span class="degree">DMD</span></p>
    <p class="doctor">Colette Margrave, <span class="degree">DMD</span></p>
    <p class="address">482 Corbett Lane, Suite 619<br>Hollis Springs, PA 17390</p>
    <ul class="contacts">
      <li>
        <svg viewBox="0 0 18 18" aria-hidden="true"><circle cx="9" cy="9" r="9" fill="var(--plum)"/><path d="M6 5.2l1.6-.4 1 2.2-1 .8c.5 1.1 1.3 1.9 2.4 2.4l.8-1 2.2 1-.4 1.6c-3.6.2-6.8-3-6.6-6.6z" fill="#fff"/></svg>
        717.555.0193
      </li>
      <li>
        <svg viewBox="0 0 18 18" aria-hidden="true"><circle cx="9" cy="9" r="9" fill="var(--plum)"/><rect x="4.5" y="6" width="9" height="6.5" fill="none" stroke="#fff" stroke-width="1.1"/><path d="M4.5 6l4.5 3.6L13.5 6" fill="none" stroke="#fff" stroke-width="1.1"/></svg>
        info@maplewoodtotsdental.example
      </li>
      <li>
        <svg viewBox="0 0 18 18" aria-hidden="true"><circle cx="9" cy="9" r="9" fill="var(--plum)"/><circle cx="9" cy="9" r="4.8" fill="none" stroke="#fff" stroke-width="1.1"/><path d="M4.2 9h9.6M9 4.2c-2.2 2.6-2.2 7 0 9.6M9 4.2c2.2 2.6 2.2 7 0 9.6" fill="none" stroke="#fff" stroke-width="1"/></svg>
        www.maplewoodtotsdental.example
      </li>
    </ul>
  </div>

  <svg class="ribbon" viewBox="0 0 700 70" aria-hidden="true">
    <polygon points="10,22 40,22 40,62 10,62 24,42" fill="var(--magenta-deep)"/>
    <polygon points="690,8 660,8 660,48 690,48 676,28" fill="var(--magenta-deep)"/>
    <polygon points="40,18 660,18 660,52 40,52" fill="var(--magenta)"/>
  </svg>
  <p class="tagline">where little smiles glow</p>
</section>

</body>
</html>
```